Wordpress website design for Pelix Bridge-Africa

We need a website for a new consultancy and digital marketplace in Kenya called 'Pelix Bridge - Africa'. Please refer to the the attached document [Pelix Bridge Africa website brief] and contact me anytime.

Bests,
Rosalind
Updates

Deadline extended to allow for additional revisions and refinements, ensuring that final designs align closely with project objectives and quality standards. This extra time will help incorporate valuable feedback and ensure the final output meets our high expectations.

Coding

```html
<!DOCTYPE html>
<html lang="en">
<head>
<meta charset="utf-8">
<title>Pelix Bridge-Africa</title>
<link href="https://fonts.googleapis.com/css2?family=Archivo:wght@500;700;800;900&family=Inter:ital,wght@0,400;0,500;0,600;0,700;1,400&display=swap" rel="stylesheet">
<style>
:root{
  --bg:#1b2b4c;
  --bg-deep:#162443;
  --card:#233862;
  --card-soft:#2b4272;
  --lime:#c9f31d;
  --lime-dark:#9fc40f;
  --white:#ffffff;
  --muted:#b7c1d6;
  --blue:#4f74c4;
}
*{margin:0;padding:0;box-sizing:border-box}
html,body{width:1200px;height:5357px;overflow:hidden}
body{background:var(--bg);color:var(--white);font-family:"Inter",sans-serif;position:relative}
.abs{position:absolute}
.display{font-family:"Archivo",sans-serif;font-weight:800;letter-spacing:-0.5px}
.eyebrow{position:absolute;font-family:"Archivo",sans-serif;font-size:10px;font-weight:700;letter-spacing:2.5px;text-transform:uppercase;display:flex;align-items:center;gap:8px}
.eyebrow::before{content:"";width:22px;height:2px;background:var(--lime)}
.photo{position:absolute;border-radius:10px}

/* nav */
.nav{position:absolute;left:83px;top:27px;width:1030px;height:56px;background:var(--card);border-radius:28px;display:flex;align-items:center;padding:0 22px}
.brand{font-family:"Archivo",sans-serif;font-weight:800;font-size:20px;color:var(--lime)}
.menu{display:flex;gap:10px;margin-left:34px}
.menu a{font-family:"Archivo",sans-serif;font-size:12px;font-weight:700;color:var(--white);text-decoration:none;padding:10px 13px;border-radius:20px}
.menu a.active{background:var(--lime);color:var(--bg)}
.nav-icons{margin-left:auto;display:flex;gap:14px}
.nav-icons span{width:32px;height:32px;border-radius:50%;background:#e9edf6;display:block}

/* hero */
.hero-title{position:absolute;left:86px;top:512px;font-size:62px;line-height:66px}
.hero-title em{font-style:normal;color:var(--lime)}
.circle-arrow{position:absolute;width:54px;height:54px;border:2px solid var(--lime);border-radius:50%;display:flex;align-items:center;justify-content:center}

/* text */
.body-text{position:absolute;font-size:15.5px;line-height:30px;color:#e4e9f3}
.h2{position:absolute;font-size:56px;line-height:60px}

/* marquee */
.band{position:absolute;left:-60px;width:1320px;transform:rotate(-2deg)}
.band.dark{background:#2b4372;height:46px}
.band.lime{background:var(--lime);height:44px;display:flex;align-items:center;gap:26px;padding-left:80px;white-space:nowrap;color:var(--bg);font-family:"Archivo",sans-serif;font-weight:800;font-size:16px;letter-spacing:0.5px}

/* services */
.svc{position:absolute;border-radius:14px;overflow:hidden}
.svc .fill{position:absolute;inset:0}
.svc-title{position:absolute;font-family:"Archivo",sans-serif;font-weight:700;font-size:16px;line-height:24px}
.mini-arrow{position:absolute;width:34px;height:34px;border-radius:50%;background:var(--lime);display:flex;align-items:center;justify-content:center}

/* products */
.prod{position:absolute;top:2610px;width:320px;height:437px;background:var(--card);border-radius:12px;overflow:hidden}
.prod .img{height:208px}
.prod h3{font-family:"Archivo",sans-serif;font-size:17px;font-weight:700;margin:18px 24px 4px}
.prod .cat{font-size:11px;color:var(--muted);margin:0 24px}
.prod .cat u{color:var(--muted)}
.prod p{font-size:13px;line-height:22px;margin:12px 24px 0;color:#e4e9f3}
.stars{display:flex;align-items:center;gap:3px;margin:18px 24px 0;font-size:12px;color:var(--blue)}
.stars i{width:13px;height:13px;background:var(--lime);clip-path:polygon(50% 0,61% 36%,100% 38%,69% 60%,80% 100%,50% 76%,20% 100%,31% 60%,0 38%,39% 36%)}
.stars b{font-weight:400;margin-left:6px}
.price{position:absolute;left:24px;bottom:22px;font-family:"Archivo",sans-serif;font-weight:700;font-size:20px}
.price small{font-family:"Inter",sans-serif;font-weight:400;font-size:11px;color:var(--muted)}
.price s{font-size:11px;font-weight:600}
.cart{position:absolute;right:0;bottom:0;width:155px;height:44px;background:var(--lime);color:var(--bg);border-radius:22px 0 12px 22px;font-family:"Archivo",sans-serif;font-weight:800;font-size:12px;letter-spacing:1px;display:flex;align-items:center;justify-content:center;gap:8px}
.cart::before{content:"";width:12px;height:12px;background:var(--bg);border-radius:2px 2px 4px 4px}

.arrows{position:absolute;display:flex;align-items:center;gap:22px}
.arrows .next{width:40px;height:40px;border-radius:50%;background:var(--lime);display:flex;align-items:center;justify-content:center}

.divider{position:absolute;left:152px;width:898px;height:3px;background:#e9edf6}

/* team */
.member{position:absolute;top:3411px;width:230px;height:358px;text-align:center;border-radius:10px}
.member.featured{background:linear-gradient(180deg,#4a6fb8 0%,#7fb23a 55%,var(--lime-dark) 100%)}
.avatar{width:156px;height:156px;border-radius:50%;border:4px solid var(--lime);margin:43px auto 0;padding:6px;background:var(--bg)}
.member.featured .avatar{background:transparent}
.avatar div{width:100%;height:100%;border-radius:50%;background:linear-gradient(180deg,#d9dde4,#8a93a3)}
.member h4{font-family:"Archivo",sans-serif;font-size:19px;font-weight:700;margin-top:34px}
.member p{font-size:12px;font-style:italic;line-height:26px;color:#dfe5f1;margin-top:6px}
.member .social{width:16px;height:16px;background:var(--lime);border-radius:3px;margin:14px auto 0}
.member.featured .social{background:#e8f3c2}

/* blog */
.post{position:absolute;border-radius:10px;overflow:hidden}
.post .title{position:absolute;left:22px;font-family:"Archivo",sans-serif;font-weight:700;font-size:18px;line-height:28px}
.chip{position:absolute;left:22px;background:var(--lime);color:var(--bg);font-size:10px;font-weight:700;padding:5px 10px;border-radius:12px;display:flex;gap:6px;align-items:center}
.chip::before{content:"";width:9px;height:9px;background:var(--bg);border-radius:2px}
.view-all{position:absolute;left:514px;top:4690px;width:172px;height:46px;border:2px solid var(--lime);border-radius:23px;display:flex;align-items:center;justify-content:center;font-family:"Archivo",sans-serif;font-weight:800;font-size:12px;letter-spacing:1.5px}

/* footer */
.fcol{position:absolute;top:5021px}
.fcol h5{font-family:"Archivo",sans-serif;font-size:12px;font-weight:800;letter-spacing:2.5px;color:var(--lime);margin-bottom:26px}
.fcol li{list-style:none;font-size:12px;color:#dfe5f1;line-height:28px}
.contact li{display:flex;gap:12px}
.contact .ico{width:10px;height:10px;background:var(--lime);border-radius:50%;margin-top:8px;flex:none}
.pay{display:flex;gap:5px}
.pay span{width:27px;height:18px;background:#e9edf6;border-radius:3px}
.footer-bottom{position:absolute;top:5295px;left:83px;width:1030px;display:flex;align-items:center}
.socials{display:flex;gap:10px;margin-left:66px}
.socials a{font-size:10px;font-weight:700;letter-spacing:0.5px;color:var(--white);text-decoration:none;border:1px solid #8a97b3;border-radius:18px;padding:10px 16px}
.copy{margin-left:auto;font-size:11px;color:var(--muted)}
.copy b{color:var(--lime);font-weight:500}
</style>
</head>
<body>

<header class="nav">
  <div class="brand">Pelix Bridge-Africa</div>
  <nav class="menu">
    <a class="active">HOME</a><a>SERVICES</a><a>DIGITAL MARKETPLACE</a><a>ABOUT US</a><a>BLOG</a><a>CONTACT</a>
  </nav>
  <div class="nav-icons"><span></span><span></span></div>
</header>

<!-- hero -->
<svg class="abs" style="left:83px;top:100px" width="1030" height="557" role="img" aria-label="Business team discussing data charts on a large screen">
  <defs><linearGradient id="heroGrad" x1="0" y1="0" x2="1" y2="1">
    <stop offset="0" stop-color="#5d7ea8"/><stop offset="0.5" stop-color="#2f4a74"/><stop offset="1" stop-color="#7a5f4e"/></linearGradient></defs>
  <path d="M12 0H1018a12 12 0 0 1 12 12V545a12 12 0 0 1-12 12H726a12 12 0 0 1-12-12V405H0V12A12 12 0 0 1 12 0Z" fill="url(#heroGrad)"/>
</svg>
<div class="eyebrow" style="left:86px;top:487px">Empowering innovations &amp;</div>
<h1 class="hero-title display">Digital Transformation<br><em>Across Africa</em></h1>
<div class="circle-arrow" style="left:711px;top:597px"><svg width="20" height="20" viewBox="0 0 20 20"><path d="M4 16L16 4M7 4h9v9" stroke="#c9f31d" stroke-width="2" fill="none"/></svg></div>

<!-- intro -->
<div class="abs" style="left:76px;top:790px;width:490px;height:380px;background:var(--lime);border-radius:10px;transform:rotate(-2deg)"></div>
<div class="photo" role="img" aria-label="Team collaborating around a table in a bright office" style="left:83px;top:805px;width:500px;height:362px;background:linear-gradient(135deg,#c5ccd6,#6b7a8e 60%,#3e4a5c)"></div>
<div class="eyebrow" style="left:616px;top:810px">Introduction</div>
<h2 class="h2 display" style="left:616px;top:828px">Pelix Bridge<br>Africa</h2>
<p class="body-text" style="left:616px;top:972px;width:500px">Pelix Bridge Africa is a consultancy firm and digital marketplace dedicated to supporting Africa's digital transformation. We provide data-driven insights, strategic guidance, customised solutions to empower public and private sectors.</p>
<p class="body-text" style="left:616px;top:1102px;width:500px">We aim to tackle complex challenges, optimize operations, and unlock growth through innovative technology.</p>

<p class="body-text" style="left:83px;top:1300px;width:510px">Our marketplace offers a curated selection of digital products and tools designed to support strategic growth, expand knowledge, strengthen data capabilities, and streamline operations. With deep expertise in digital transformation and a focus on Africa's unique opportunities, Pelix Bridge Africa is your trusted partner in navigating today's dynamic digital landscape.</p>
<p class="body-text" style="left:83px;top:1492px;width:510px">Together, we're advancing Africa's digital future.</p>
<div class="abs" style="left:626px;top:1222px;width:496px;height:380px;background:var(--lime);border-radius:10px;transform:rotate(-2deg)"></div>
<div class="photo" role="img" aria-label="Woman working on a laptop with glowing digital network icons" style="left:624px;top:1233px;width:490px;height:358px;background:linear-gradient(135deg,#cdd2d8,#9aa3ad 50%,#b8763a)"></div>

<!-- marquee 1 -->
<div class="band dark" style="top:1712px"></div>
<div class="band lime" style="top:1752px">
  <span>CONSULTANCY FIRM</span><span>✳</span><span>DIGITAL MARKETPLACE</span><span>✳</span><span>CONSULTANCY FIRM</span><span>✳</span><span>DIGITAL MARKETPLACE</span><span>✳</span><span>CONSULTANCY FIRM</span>
</div>

<!-- services -->
<div class="eyebrow" style="left:534px;top:1903px">Services</div>
<h2 class="h2 display" style="left:0;width:1200px;text-align:center;top:1925px">What We Do</h2>

<div class="svc" style="left:83px;top:2053px;width:240px;height:297px;background:var(--bg)">
  <div class="fill" role="img" aria-label="Presenter explaining a strategy board" style="background:linear-gradient(160deg,#3b4e6c,#b8c0cc 55%,#5a6578);bottom:60px"></div>
</div>
<div class="svc-title" style="left:83px;top:2325px">Digital Strategy</div>
<div class="mini-arrow" style="left:286px;top:2058px"><svg width="14" height="14"><path d="M2 12L12 2M5 2h7v7" stroke="#1b2b4c" stroke-width="2" fill="none"/></svg></div>

<div class="svc" style="left:349px;top:2018px;width:238px;height:368px">
  <div class="fill" role="img" aria-label="Team working together at laptops" style="background:linear-gradient(160deg,#4a4a42,#c3b5a4 50%,#4c5364)"></div>
</div>
<div class="svc-title" style="left:349px;top:2360px">Technical Expertise</div>
<div class="mini-arrow" style="left:548px;top:2023px"><svg width="14" height="14"><path d="M2 12L12 2M5 2h7v7" stroke="#1b2b4c" stroke-width="2" fill="none"/></svg></div>

<div class="svc" style="left:612px;top:2053px;width:238px;height:297px;background:linear-gradient(180deg,#6eb541,#3b6f8e 80%,#2f5a8a)" role="img" aria-label="Data analytics on screens">
  <div class="abs" style="left:94px;top:98px;width:50px;height:50px;border-radius:50%;border:2px solid #fff;display:flex;align-items:center;justify-content:center"><svg width="18" height="18"><path d="M3 15L15 3M6 3h9v9" stroke="#fff" stroke-width="2" fill="none"/></svg></div>
</div>
<div class="svc-title" style="left:612px;top:2325px">Data Analytics</div>

<div class="svc" style="left:876px;top:2018px;width:238px;height:368px">
  <div class="fill" role="img" aria-label="Engineer working with an AI model on a monitor" style="background:linear-gradient(160deg,#1d2c48,#2f6b9a 50%,#3b3fa0)"></div>
</div>
<div class="svc-title" style="left:876px;top:2360px">Artificial Intelligence (AI)<br>&amp; Machine Learning (ML)</div>
<div class="mini-arrow" style="left:1074px;top:2023px"><svg width="14" height="14"><path d="M2 12L12 2M5 2h7v7" stroke="#1b2b4c" stroke-width="2" fill="none"/></svg></div>

<!-- products -->
<div class="eyebrow" style="left:90px;top:2513px">Marketplace</div>
<h2 class="h2 display" style="left:120px;top:2528px">Our Products</h2>
<div class="arrows" style="left:1036px;top:2532px">
  <svg width="16" height="12"><path d="M15 6H2M6 2L2 6l4 4" stroke="#fff" stroke-width="1.5" fill="none"/></svg>
  <div class="next"><svg width="18" height="14"><path d="M1 7h15M11 2l5 5-5 5" stroke="#1b2b4c" stroke-width="2" fill="none"/></svg></div>
</div>

<div class="prod" style="left:83px">
  <div class="img" role="img" aria-label="Website template layouts" style="background:linear-gradient(135deg,#e8ebef,#b9c3cc 60%,#4a6b5a)"></div>
  <h3>Templates</h3><div class="cat">in <u>Strategy</u></div>
  <p>Curabitur venenis au non varius tincidunt. Suspendisse grida est eget ipsum aliquet pellentesque.</p>
  <div class="stars"><i></i><i></i><i></i><i></i><i></i><b>135 reviews</b></div>
  <div class="price">$ 62 <small>/lifetime <s>$88</s></small></div>
  <div class="cart">ADD TO CART</div>
</div>
<div class="prod" style="left:441px">
  <div class="img" role="img" aria-label="Phone resting on an open book" style="background:linear-gradient(135deg,#f1ede6,#d8cdbd 60%,#a99880)"></div>
  <h3>e-books</h3><div class="cat">in <u>Strategy</u></div>
  <p>Curabitur venenis au non varius tincidunt. Suspendisse grida est eget ipsum aliquet pellentesque.</p>
  <div class="stars"><i></i><i></i><i></i><i></i><i></i><b>135 reviews</b></div>
  <div class="price">$ 75 <small>/lifetime <s>$88</s></small></div>
  <div class="cart">ADD TO CART</div>
</div>
<div class="prod" style="left:795px">
  <div class="img" role="img" aria-label="Desk with laptops showing code" style="background:linear-gradient(135deg,#3b4656,#a69a88 55%,#d9d2c6)"></div>
  <h3>Software</h3><div class="cat">in <u>Strategy</u></div>
  <p>Curabitur venenis au non varius tincidunt. Suspendisse grida est eget ipsum aliquet pellentesque.</p>
  <div class="stars"><i></i><i></i><i></i><i></i><i></i><b>135 reviews</b></div>
  <div class="price">$ 99 <small>/lifetime <s>$105</s></small></div>
  <div class="cart">ADD TO CART</div>
</div>

<div class="divider" style="top:3148px"></div>

<!-- team -->
<div class="eyebrow" style="left:90px;top:3270px">Team</div>
<h2 class="h2 display" style="left:120px;top:3288px">Meet Our Team</h2>
<div class="arrows" style="left:1036px;top:3305px">
  <svg width="16" height="12"><path d="M15 6H2M6 2L2 6l4 4" stroke="#fff" stroke-width="1.5" fill="none"/></svg>
  <div class="next"><svg width="18" height="14"><path d="M1 7h15M11 2l5 5-5 5" stroke="#1b2b4c" stroke-width="2" fill="none"/></svg></div>
</div>

<div class="member" style="left:99px"><div class="avatar"><div role="img" aria-label="Portrait of Dorian Kell"></div></div><h4>Dorian Kell</h4><p>Chatered Management Accountant<br>(ACFA, CMFA)</p><div class="social"></div></div>
<div class="member" style="left:355px"><div class="avatar"><div role="img" aria-label="Portrait of Mira Osten"></div></div><h4>Mira Osten</h4><p>Chatered Management Accountant<br>(ACFA, CMFA)</p><div class="social"></div></div>
<div class="member featured" style="left:612px"><div class="avatar"><div role="img" aria-label="Portrait of Kaleb Arno"></div></div><h4>Kaleb Arno</h4><p>Chatered Management Accountant<br>(ACFA, CMFA)</p><div class="social"></div></div>
<div class="member" style="left:867px"><div class="avatar"><div role="img" aria-label="Portrait of Selma Varin"></div></div><h4>Selma Varin</h4><p>Chatered Management Accountant<br>(ACFA, CMFA)</p><div class="social"></div></div>

<div class="divider" style="top:3884px"></div>

<!-- blog -->
<div class="eyebrow" style="left:550px;top:4017px">Blog</div>
<h2 class="h2 display" style="left:0;width:1200px;text-align:center;top:4035px">Latest Blog &amp; Articles</h2>

<div class="post" style="left:158px;top:4123px;width:435px;height:560px" role="img" aria-label="Colleagues shaking hands in a meeting">
  <div class="abs" style="inset:0;background:linear-gradient(180deg,#c9cfd6 0%,#7d8796 55%,#1e2e4e 100%)"></div>
  <div class="chip" style="top:4435px;top:432px">OCT. 20, 2024</div>
  <div class="title" style="top:462px">Nunc sodales lectus sit amet augue<br>egestas, eget tincidunt sapien</div>
</div>
<div class="post" style="left:612px;top:4123px;width:428px;height:239px" role="img" aria-label="Team reviewing work at a laptop">
  <div class="abs" style="inset:0;background:linear-gradient(180deg,#6d7688,#2a3a5a 80%)"></div>
  <div class="chip" style="top:150px">OCT. 20, 2024</div>
  <div class="title" style="top:176px">Nunc sodales lectus sit amet augue<br>egestas, eget tincidunt sapien</div>
</div>
<div class="post" style="left:612px;top:4389px;width:428px;height:239px" role="img" aria-label="Online shopping concept">
  <div class="abs" style="inset:0;background:linear-gradient(120deg,#5e9a3c,#2f4f86 70%,#3a5da0)"></div>
  <div class="chip" style="top:140px">OCT. 20, 2024</div>
  <div class="title" style="top:166px">Nunc sodales lectus sit amet augue<br>egestas, eget tincidunt sapien</div>
</div>
<div class="view-all">VIEW ALL ↗</div>

<!-- marquee 2 -->
<div class="band dark" style="top:4810px"></div>
<div class="band lime" style="top:4850px">
  <span>CONSULTANCY FIRM</span><span>✳</span><span>DIGITAL MARKETPLACE</span><span>✳</span><span>CONSULTANCY FIRM</span><span>✳</span><span>DIGITAL MARKETPLACE</span><span>✳</span><span>CONSULTANCY FIRM</span>
</div>

<!-- footer -->
<div class="fcol" style="left:83px"><h5>QUICK LINKS</h5><ul><li>Home</li><li>Services</li><li>Digital Marketplace</li><li>About Us</li><li>Blog</li><li>Contact</li></ul></div>
<div class="fcol" style="left:285px"><h5>ACCOUNT LOGIN</h5><ul><li>Create Account</li><li>Orders</li><li>Favorites List</li><li>Coparison List</li></ul></div>
<div class="fcol" style="left:503px"><h5>FIND OUT</h5><ul><li>How to order</li><li>Shipping Methods</li><li>Payment methods</li><li>Return &amp; cancellation</li></ul></div>
<div class="fcol contact" style="left:720px"><h5>CONTACT INFO</h5><ul><li><span class="ico"></span><span>Mango Rd, Kileleshwa,<br>Nairobi Kenya</span></li><li><span class="ico"></span>1800-555-019</li><li><span class="ico"></span>info@pelixbridgeafrica.com</li></ul></div>
<div class="fcol" style="left:951px"><h5>PAYMENT METHOD</h5><div class="pay"><span></span><span></span><span></span><span></span><span></span></div></div>

<div class="footer-bottom">
  <div class="brand">Pelix Bridge-Africa</div>
  <div class="socials"><a>LINKORA</a><a>FACEFOLD</a><a>CHIRPER</a><a>SNAPGRAM</a><a>CLIPTOK</a></div>
  <div class="copy">© 2024 <b>Pelix Bridge-Africa</b>. All right reserved</div>
</div>

</body>
</html>
```